Time for a new business card design

We need a new business card design for Torvel Furniture Rentals based in Australia. www.torvel-example.com.au. We specialise in providing furniture rentals for home staging, corporate relocations events and product launches etc. We would like to see designs that include our logo on the front of the card with all the standard contact details as well as having a realy nice image on the back with a list of our services we offer. Our logo is red and this cannot change. Were looking for a pallet of red and white with maybe a splash of grey. The final design should communication organised & stylish. We are in the process of finalising our new website and would like the card design to compliment this as well

Industry/Entity Type

Communication

Requirements
Must have
• Square corners
logo
name, title, email, phone, address
image on back of card with space for list of services we offer
Services:
•Furniture and appliance rental
•Property styling
•Events and functions
•Office furniture rental

The card must be landscape.
The image is to appear on the back of the card only.

```html
<!DOCTYPE html>
<html lang="en">
<head>
<meta charset="utf-8">
<title>Torvel Furniture Rentals – Business Card</title>
<link rel="stylesheet" href="https://fonts.googleapis.com/css2?family=Noto+Sans:wght@400;500&display=swap">
<style>
  :root {
    --brand-red: #c8082a;
    --white: #ffffff;
    --mist: #dcdcdc;
    --ink: #111111;
    --divider-light: #e6e6e6;
    --divider-dark: #a8a8a8;
    --canvas: #ffffff;
  }
  * { box-sizing: border-box; margin: 0; padding: 0; }
  html, body { width: 1200px; height: 831px; overflow: hidden; background: var(--canvas); }
  body { position: relative; font-family: "Noto Sans", sans-serif; color: var(--ink); }

  .card {
    position: absolute;
    left: 290px;
    width: 612px;
    height: 340px;
    overflow: hidden;
    background: linear-gradient(to bottom,
      var(--mist) 0%, var(--white) 14%, var(--white) 50%,
      #f2c4cc 60%, var(--brand-red) 80%, var(--brand-red) 100%);
  }
  .card--front { top: 61px; }
  .card--back { top: 428px; }

  .freecall {
    position: absolute;
    right: 28px;
    top: 20px;
    font-size: 20px;
  }
  .wordmark {
    position: absolute;
    left: 52px;
    top: 80px;
    font-size: 43px;
    font-weight: 500;
    color: var(--brand-red);
    letter-spacing: -0.5px;
    white-space: nowrap;
  }

  .branch {
    position: absolute;
    top: 182px;
  }
  .branch--sydney { left: 22px; }
  .branch--brisbane { left: 211px; }
  .branch--melbourne { left: 410px; }
  .branch__city { font-size: 21px; font-weight: 400; margin-bottom: 16px; }
  .branch__line { font-size: 11.5px; line-height: 17px; letter-spacing: 0.2px; white-space: nowrap; }

  .divider {
    position: absolute;
    top: 190px;
    width: 6px;
    height: 112px;
    background: linear-gradient(to bottom, var(--divider-dark), var(--divider-light));
  }
  .divider--one { left: 193px; }
  .divider--two { left: 390px; }

  .services__title {
    position: absolute;
    left: 72px;
    top: 56px;
    font-size: 29px;
    font-weight: 400;
  }
  .services__list {
    position: absolute;
    left: 24px;
    top: 128px;
    list-style: none;
    font-size: 20px;
    line-height: 26px;
    white-space: nowrap;
  }
  .services__list li { padding-left: 12px; text-indent: -12px; }
  .services__list li::before { content: "•"; }

  .photo-slot {
    position: absolute;
    left: 285px;
    top: 78px;
    width: 302px;
    height: 202px;
    background: linear-gradient(to bottom, #c9dced 0%, #e8eef2 35%, #f1b9c3 65%, #e9707f 100%);
  }
</style>
</head>
<body>
  <section class="card card--front" aria-label="Card front">
    <p class="freecall">Freecall today 1800 55 01 99</p>
    <h1 class="wordmark">Torvel Furniture Rentals</h1>

    <div class="branch branch--sydney">
      <h2 class="branch__city">Sydney</h2>
      <p class="branch__line">2/318 Larkmoor Road</p>
      <p class="branch__line">Alexandria NSW 2015</p>
      <p class="branch__line">Phone 02 9000 4172</p>
      <p class="branch__line">syd@torvel-example.com.au</p>
    </div>
    <span class="divider divider--one"></span>
    <div class="branch branch--brisbane">
      <h2 class="branch__city">Brisbane</h2>
      <p class="branch__line">58 Fenwick Road</p>
      <p class="branch__line">East Brisbane, QLD 4169</p>
      <p class="branch__line">Phone 07 3000 6815</p>
      <p class="branch__line">bne@torvel-example.com.au</p>
    </div>
    <span class="divider divider--two"></span>
    <div class="branch branch--melbourne">
      <h2 class="branch__city">Melbourne</h2>
      <p class="branch__line">19 Ashgrove Road</p>
      <p class="branch__line">Hawthorn East VIC 3123</p>
      <p class="branch__line">Phone 03 9000 2739</p>
      <p class="branch__line">mel@torvel-example.com.au</p>
    </div>
  </section>

  <section class="card card--back" aria-label="Card back">
    <h2 class="services__title">Services:</h2>
    <ul class="services__list">
      <li>Furniture and<br>appliance rental</li>
      <li>Property styling</li>
      <li>Events and functions</li>
      <li>Office furniture rental</li>
    </ul>
    <div class="photo-slot" role="img" aria-label="Photo of a bright styled bedroom with pink bedding, cushions and a sea view window"></div>
  </section>
</body>
</html>
```